Luxury Wine Label for New Startup Winery

We need a wine label for our new winery startup. We have worked with a local designer but do not feel the resulting label / logo have the elevation required to present our brand as a luxury wine. Our winery is called "Harrowgate Vineyards" and we are focused on extremely high quality hand crafted artisan and estate wines from the Pacific Northwest.
We would like to see designs that utilize a tree line, or other imagery that represents the "Harrowgate" part of our company name. Another interesting feature could be wood grain.
A logo will be required based on your design so please design with this in mind:
This logo should be consistent with the wine bottle label design, and should be representative of our high end exclusive wine while giving a sense of place (Oregon/ Pacific Northwest.)
I will supply an image of the design we received from our local designer, PLEASE NOTE: in general we do like wood grain and tree line concepts but feel the execution was poorly done.
ATTN: Logo design should be suitable for use on: Bottles (Red wine/rose/white wine), Bussiness cards, vehicle signage, business signage, etc
P.S.:
If you have a design that is not outside the box we are still interested in seeing it.
Label is for a burgundy style bottle with a label height of 3.5 - 4" and a width of 3.5-4"
any label <= 4"x4" and >=3.5"x3.5" will be acceptable:
HOWEVER Width should be greater than or equal to height due to the bottle format
Target Market(s)
Wine enthusiasts with adequate discretionary budgets to afford $100 bottles of wine.
Industry/Entity Type
Wine / Winery
Requirements
Must have
- A sense of luxury, a feel of exclusivity, and a theme consistent with our product and brand name
Nice to have
- Tree line, wood grain or other wood themes. Serif fonts
Should not have
- anything cheesy, off topic, hard to read script fonts or anything that makes the label hard to read from a few feet away or too busy

```html
<!DOCTYPE html>
<html lang="en">
<head>
<meta charset="UTF-8">
<title>Harrowgate Vineyards — Rosé Label</title>
<link rel="stylesheet" href="https://fonts.googleapis.com/css2?family=EB+Garamond:wght@400;500&display=swap">
<style>
  :root {
    --stage: #2e1820;
    --label: #222021;
    --grain-soft: #2e2a27;
    --grain-warm: #4a3f34;
    --ink-sand: #c7b3a1;
    --ink-rose: #c0426a;
  }
  * { margin: 0; padding: 0; box-sizing: border-box; }
  html, body {
    width: 1200px;
    height: 1200px;
    overflow: hidden;
    background: var(--stage);
  }
  .canvas {
    position: relative;
    width: 1200px;
    height: 1200px;
    background: var(--stage);
  }
  .label {
    position: absolute;
    left: 150px;
    top: 160px;
    width: 900px;
    height: 880px;
    background: var(--label);
    overflow: hidden;
    font-family: "EB Garamond", Georgia, serif;
    text-align: center;
  }
  .label__grain {
    position: absolute;
    inset: 0;
    background:
      radial-gradient(ellipse 36% 40% at 50% 48%, var(--label) 0%, var(--label) 62%, rgba(34,32,33,0) 100%),
      radial-gradient(ellipse 75% 75% at 50% 50%, var(--grain-soft) 0%, var(--grain-soft) 45%, var(--grain-warm) 100%);
  }
  .brand-mark {
    position: absolute;
    left: 50%;
    top: 212px;
    width: 34px;
    height: 34px;
    margin-left: -17px;
    border-radius: 50%;
    background: var(--ink-sand);
  }
  .wordmark {
    position: absolute;
    left: 0;
    right: 0;
    top: 282px;
    color: var(--ink-sand);
    font-weight: 400;
    line-height: 1;
  }
  .wordmark__name {
    display: block;
    font-size: 52px;
    letter-spacing: 0.01em;
  }
  .wordmark__sub {
    display: block;
    margin-top: 8px;
    font-size: 40px;
    letter-spacing: 0.16em;
  }
  .varietal {
    position: absolute;
    left: 0;
    right: 0;
    top: 572px;
    color: var(--ink-rose);
    font-size: 76px;
    font-weight: 400;
    letter-spacing: 0.02em;
    line-height: 1;
  }
</style>
</head>
<body>
  <main class="canvas">
    <section class="label">
      <div class="label__grain" role="img" aria-label="Fine sand-coloured wood-grain contour lines swirling in from the label edges around a plain dark centre"></div>
      <span class="brand-mark"></span>
      <h1 class="wordmark">
        <span class="wordmark__name">HARROWGATE</span>
        <span class="wordmark__sub">VINEYARDS</span>
      </h1>
      <p class="varietal">ROSÉ</p>
    </section>
  </main>
</body>
</html>
```